Flair Bartenders Website Needs an Overhaul

We are a group of flair bartenders based in San Diego that provide a fun bartending alternative to private parties and events. We haven’t changed our website design in a long time and need to bring our current flash based website in line with the times and go to HTML5 (see our website www.pourvortexcrew.com).

We have a “skateboard grunge” theme to our current website and would like to keep that look as our pictures and video are all taken in an urban setting. We are not married to any particular colors and want to have a “rock star” feel to the site as it needs to attract people that like to party!

Find in the files our logo and the font file.
Updates

Target Market(s)

Our clients are fun, outgoing individuals where normal lines are blurred and risks are taken.

Industry/Entity Type

Events

Number of Pages Required

4 page

Requirements
Must have
• An urban skateboarding feel.
Nice to have
• Keep the green theme, although not essential.
Should not have
• No "business type" "corporate" websites.. BORING!!

```html
<!DOCTYPE html>
<html lang="en">
<head>
<meta charset="utf-8">
<title>Pour Vortex – Flair Bartenders San Diego</title>
<link href="https://fonts.googleapis.com/css2?family=Open+Sans:wght@300;400;600;700;800&display=swap" rel="stylesheet">
<style>
:root{
  --ink:#1d1d1d;
  --header:#141414;
  --footer:#1a1a1a;
  --footer-deep:#0f0f0f;
  --accent:#e8661c;
  --accent-dark:#c9540f;
  --paper:#ffffff;
  --grey:#e6e6e6;
  --muted:#9a9a9a;
  --text:#333333;
}
*{margin:0;padding:0;box-sizing:border-box}
html,body{width:758px;height:1200px;overflow:hidden}
body{font-family:"Open Sans",Arial,sans-serif;color:var(--text);background:var(--paper);position:relative}

/* header */
.site-header{position:absolute;top:0;left:0;width:758px;height:70px;background:var(--header);display:flex;align-items:center;justify-content:space-between;padding:0 40px}
.brand{color:#fff;font-weight:800;font-size:22px;letter-spacing:.5px;display:flex;align-items:center;gap:8px}
.brand-dot{width:10px;height:10px;background:var(--accent)}
.main-nav{display:flex;gap:14px}
.main-nav a{color:#d8d8d8;text-decoration:none;font-size:9.5px;font-weight:600;letter-spacing:.4px}
.main-nav a.active{color:var(--accent)}

/* hero */
.hero{position:absolute;top:70px;left:0;width:758px;height:448px;background:radial-gradient(ellipse at 40% 30%,#9a9ea6 0%,#5d6068 40%,#2a2b30 100%)}
.packages-panel{position:absolute;left:435px;top:228px;width:298px;height:184px;background:rgba(20,14,10,.82);padding:16px 18px}
.packages-panel h2{color:var(--accent);font-weight:400;font-size:30px;margin-bottom:12px;line-height:1}
.panel-list{display:grid;grid-template-columns:repeat(3,auto);gap:8px 10px;list-style:none;justify-content:start}
.panel-list li{color:#fff;font-size:9px;font-weight:700;letter-spacing:.3px}
.btn{display:inline-block;font-weight:600;text-decoration:none;letter-spacing:.3px}
.btn-accent{background:var(--accent);color:#fff}
.btn-dark{background:var(--ink);color:#fff}
.packages-panel .btn{margin-top:16px;font-size:10px;padding:8px 12px}

/* welcome */
.welcome{position:absolute;top:518px;left:0;width:758px;height:215px;text-align:center;padding-top:28px}
.welcome h1{font-weight:300;font-size:34px;color:var(--ink);margin-bottom:14px}
.welcome p{width:640px;margin:0 auto;font-size:9px;line-height:1.55;color:#444}
.welcome-actions{margin-top:20px;display:flex;justify-content:center;gap:12px}
.welcome-actions .btn{font-size:16px;padding:8px 22px;font-weight:400}

/* package cards */
.packages{position:absolute;top:733px;left:0;width:758px;height:265px;background:var(--grey);text-align:center}
.packages h2{font-weight:300;font-size:32px;color:var(--ink);margin-top:26px}
.card-row{position:absolute;top:81px;left:40px;width:678px;display:flex;gap:6px}
.card{width:108px;height:159px;background:var(--paper);display:flex;flex-direction:column}
.card-label{height:44px;display:flex;align-items:center;justify-content:center;font-size:9px;font-weight:700;color:var(--ink);padding:0 6px;line-height:1.3}
.card-photo{flex:1}
.card.label-bottom{flex-direction:column-reverse}
.photo-warm{background:linear-gradient(160deg,#8a5a3c,#3b2a22)}
.photo-cool{background:linear-gradient(160deg,#7d8694,#3a3f48)}
.photo-blue{background:linear-gradient(160deg,#5a6f9a,#26324a)}
.photo-night{background:linear-gradient(160deg,#4a4040,#141212)}

/* footer */
.site-footer{position:absolute;top:998px;left:0;width:758px;height:202px;background:var(--footer);color:#cfcfcf}
.footer-cols{position:absolute;top:18px;left:40px;width:678px;display:flex;gap:30px}
.footer-brand{width:170px}
.footer-brand .brand{font-size:19px;margin-bottom:12px}
.footer-brand address{font-style:normal;font-size:9px;line-height:1.5;color:#bdbdbd}
.footer-col h3{font-size:9px;font-weight:700;color:#fff;letter-spacing:.4px;margin-bottom:8px}
.footer-links{list-style:none;width:110px}
.footer-links li{font-size:9px;color:var(--accent);line-height:1.55}
.gallery{display:grid;grid-template-columns:repeat(4,24px);gap:4px}
.gallery span{height:22px;background:linear-gradient(150deg,#8a4ad0,#3a1d6a)}
.map{width:150px;height:90px;background:linear-gradient(135deg,#d9d4c4,#a9c4d8)}
.footer-call{position:absolute;left:40px;top:138px;font-size:14px;font-weight:700;color:#fff;letter-spacing:.3px}
.footer-bottom{position:absolute;bottom:0;left:0;width:758px;height:34px;background:var(--footer-deep);display:flex;align-items:center;justify-content:space-between;padding:0 40px;font-size:8px;color:var(--muted)}
</style>
</head>
<body>

<header class="site-header">
  <div class="brand"><span class="brand-dot"></span>Pour Vortex</div>
  <nav class="main-nav">
    <a href="#" class="active">HOME</a>
    <a href="#">ABOUT US</a>
    <a href="#">PACKAGES</a>
    <a href="#">CREW</a>
    <a href="#">MEDIA</a>
    <a href="#">GET QUOTE</a>
    <a href="#">FAN CLUB</a>
  </nav>
</header>

<section class="hero" role="img" aria-label="Flair bartender in a black t-shirt tossing a bottle against a grey studio backdrop">
  <div class="packages-panel">
    <h2>Our Packages</h2>
    <ul class="panel-list">
      <li>WORKING</li>
      <li>COCKTAILS &amp; DREAMS</li>
      <li>EXHIBITIONS</li>
      <li>FLAIR TRAINING</li>
      <li>PORTABLE BARS</li>
      <li></li>
      <li>COMPETITIONS</li>
      <li>ICE BARS</li>
    </ul>
    <a href="#" class="btn btn-accent">GET A QUOTE</a>
  </div>
</section>

<section class="welcome">
  <h1>Welcome to Pour Vortex</h1>
  <p>The Pour Vortex crew are San Diego's top flair bartenders brought to your event and blended together with a dedication to service, mixology and entertainment. This is a fun alternative to traditional bartending that will provide your guests with specialized personal crowd interaction plus an unforgettable flair show. Audiences are very receptive to this practical form of entertainment and it blends well in conjunction with live bands, DJs and fun events.</p>
  <div class="welcome-actions">
    <a href="#" class="btn btn-dark">GET A QUOTE</a>
    <a href="#" class="btn btn-accent">CALL US - 1.619.555.0142</a>
  </div>
</section>

<section class="packages">
  <h2>Our Packages</h2>
  <div class="card-row">
    <article class="card">
      <div class="card-label">WORKING</div>
      <div class="card-photo photo-warm" role="img" aria-label="Bartenders working behind a bar"></div>
    </article>
    <article class="card label-bottom">
      <div class="card-label">COCKTAILS &amp; DREAMS EXPERIENCE</div>
      <div class="card-photo photo-night" role="img" aria-label="Cocktail party crowd"></div>
    </article>
    <article class="card">
      <div class="card-label">EXHIBITIONS</div>
      <div class="card-photo photo-blue" role="img" aria-label="Flair exhibition on stage"></div>
    </article>
    <article class="card label-bottom">
      <div class="card-label">FLAIR TRAINING</div>
      <div class="card-photo photo-cool" role="img" aria-label="Flair training session with bottles"></div>
    </article>
    <article class="card">
      <div class="card-label">PORTABLE BARS</div>
      <div class="card-photo photo-night" role="img" aria-label="Portable bar set up for an event"></div>
    </article>
    <article class="card label-bottom">
      <div class="card-label">COMPETITIONS</div>
      <div class="card-photo photo-warm" role="img" aria-label="Bartender at a flair competition"></div>
    </article>
    <article class="card">
      <div class="card-label">ICE BARS</div>
      <div class="card-photo photo-cool" role="img" aria-label="Bartender behind a sculpted ice bar"></div>
    </article>
  </div>
</section>

<footer class="site-footer">
  <div class="footer-cols">
    <div class="footer-brand">
      <div class="brand"><span class="brand-dot"></span>Pour Vortex</div>
      <address>2710 Canyon Ridge Road<br>San Diego California<br>92108<br>Tel 1.619.555.0142</address>
    </div>
    <div class="footer-col">
      <h3>PACKAGES</h3>
      <ul class="footer-links">
        <li>Working</li>
        <li>Cocktails &amp; Dreams</li>
        <li>Exhibitions</li>
        <li>Flair Training</li>
        <li>Portable Bars</li>
        <li>Competitions</li>
        <li>Ice Bars</li>
      </ul>
    </div>
    <div class="footer-col">
      <h3>PHOTO GALLERY</h3>
      <div class="gallery" role="img" aria-label="Thumbnails of event photos">
        <span></span><span></span><span></span><span></span>
        <span></span><span></span><span></span><span></span>
        <span></span><span></span><span></span><span></span>
      </div>
    </div>
    <div class="footer-col">
      <h3>OUR LOCATION</h3>
      <div class="map" role="img" aria-label="Map of San Diego showing the crew's location"></div>
    </div>
  </div>
  <div class="footer-call">CALL US - 1.619.555.0142</div>
  <div class="footer-bottom">
    <span>Copyright © 2015 Pour Vortex</span>
    <span>Privacy Policy</span>
  </div>
</footer>

</body>
</html>
```